A card that says it all!

Hey there!
We are in need of a business card design for a facility service provider company named Kelbrook Works.
I would like a business card design that is not focus on a person but more on the company. A place for a QR code would be nice, and i will have that code direct to our request form online. "Scanner to schedule service" or "Scan to schedule a estimate". Something like that. Kelbrook Works is the Industry Leader in Facility Remodeling, Rollouts, and Capital Repairs

Target Market(s)

large facilities needing services such as remodels. HVAC, plumbing, electrical

Industry/Entity Type

Industry Leader in Facility Remodeling, Rollouts, and Capital Repairs

Contact Information for Business Card

phone number: 418.527.3096; email: info@kelbrookworks.us; Website: www.KelbrookWorks.us

Requirements
Must have
• sleak; classic
Should not have
• No houses or tools art

```html
<!DOCTYPE html>
<html lang="en">
<head>
<meta charset="utf-8">
<title>Kelbrook Works – Business Card</title>
<link rel="stylesheet" href="https://fonts.googleapis.com/css2?family=Playfair+Display:wght@400&family=Poppins:wght@600&display=swap">
<style>
  :root {
    --brand-blue: #1f4aa0;
    --frame-red: #e3262b;
    --paper: #ffffff;
  }
  * { margin: 0; padding: 0; box-sizing: border-box; }
  html, body {
    width: 1200px;
    height: 686px;
    overflow: hidden;
    background: var(--paper);
  }
  .card {
    position: relative;
    width: 1200px;
    height: 686px;
    background: var(--paper);
    color: var(--brand-blue);
    font-family: "Playfair Display", serif;
  }
  .company-name {
    position: absolute;
    left: 73px;
    top: 58px;
    font-weight: 400;
    line-height: 1;
    white-space: nowrap;
  }
  .company-name .name-lead {
    font-size: 84px;
    letter-spacing: -1px;
  }
  .company-name .name-tail {
    font-size: 44px;
    margin-left: 6px;
  }
  .tagline {
    position: absolute;
    left: 73px;
    top: 160px;
    font-size: 35px;
    line-height: 52px;
    font-weight: 400;
  }
  .contact-list {
    position: absolute;
    left: 171px;
    top: 464px;
    list-style: none;
    font-size: 39px;
    line-height: 53px;
  }
  .brand-mark {
    position: absolute;
    right: 41px;
    top: 52px;
    text-align: right;
    font-size: 38px;
    line-height: 42px;
    font-weight: 400;
  }
  .qr-placeholder {
    position: absolute;
    left: 877px;
    top: 354px;
    width: 282px;
    height: 282px;
    border: 3px solid var(--frame-red);
    border-radius: 4px;
    display: flex;
    flex-direction: column;
    align-items: center;
    justify-content: center;
    font-family: "Poppins", sans-serif;
    font-weight: 600;
    font-size: 51px;
    line-height: 66px;
    color: var(--brand-blue);
    padding-top: 6px;
  }
</style>
</head>
<body>
  <main class="card">
    <h1 class="company-name"><span class="name-lead">Kelbrook</span><span class="name-tail">Works</span></h1>
    <p class="tagline">is the Industry Leader in Facility<br>Remodeling, Rollouts, and<br>Capital Repairs</p>

    <ul class="contact-list">
      <li class="contact-phone">418.527.3096</li>
      <li class="contact-email">info@kelbrookworks.us</li>
      <li class="contact-web">www.KelbrookWorks.us</li>
    </ul>

    <div class="brand-mark">Kelbrook<br>Works</div>

    <div class="qr-placeholder">
      <span>QR</span>
      <span>CODE</span>
    </div>
  </main>
</body>
</html>
```